Re-Branding

I would like a new "brand" which will incorporate my new photo. I do title insurance in California for Harborline Deed Assurance Corp. Could be used on business cards or flyers.

Target Market(s)

Real Estate Professionals, Attorneys, Mortgage Companies and Banks.

Contact Information for Business Card

High Gloss

Requirements
Must have
• My photo, my logo and my contact information.
Nice to have
• background that is appealing to clients
Should not have
• home email address

```html
<!DOCTYPE html>
<html lang="en">
<head>
<meta charset="utf-8">
<title>Marisa Delgado — Harborline Deed Assurance Corp.</title>
<link href="https://fonts.googleapis.com/css2?family=Bodoni+Moda:wght@500;600&family=Mulish:wght@500&display=swap" rel="stylesheet">
<style>
  :root {
    --navy: #14214f;
    --green: #1c6b2c;
    --green-rule: #2f7d3a;
    --paper-top: #ffffff;
    --paper-bottom: #eeeeef;
    --portrait-light: #d9c3a5;
    --portrait-dark: #1d8a40;
  }
  html, body {
    margin: 0;
    padding: 0;
    overflow: hidden;
    background: #ffffff;
  }
  .card {
    position: relative;
    width: 1200px;
    height: 771px;
    overflow: hidden;
    background: linear-gradient(180deg, var(--paper-top) 0%, var(--paper-bottom) 100%);
    font-family: "Mulish", sans-serif;
    color: var(--navy);
  }
  .card__shapes {
    position: absolute;
    inset: 0;
  }
  .card__portrait {
    position: absolute;
    left: 622px;
    top: 62px;
    width: 471px;
    height: 709px;
    border-radius: 180px 180px 0 0;
    background: linear-gradient(180deg, var(--portrait-light) 0%, var(--portrait-light) 42%, var(--portrait-dark) 56%, var(--portrait-dark) 100%);
  }
  .card__name {
    position: absolute;
    left: 112px;
    top: 168px;
    margin: 0;
    font-family: "Bodoni Moda", serif;
    font-weight: 500;
    font-size: 68px;
    line-height: 1;
    letter-spacing: 0.5px;
  }
  .card__title {
    position: absolute;
    left: 117px;
    top: 274px;
    margin: 0;
    font-size: 25px;
    letter-spacing: 0.6px;
  }
  .card__rule {
    position: absolute;
    left: 116px;
    top: 322px;
    width: 501px;
    height: 2px;
    background: var(--green-rule);
  }
  .card__phone {
    position: absolute;
    left: 118px;
    top: 392px;
    margin: 0;
    font-family: "Bodoni Moda", serif;
    font-weight: 600;
    font-size: 54px;
    line-height: 1;
    letter-spacing: 1px;
  }
  .card__links {
    position: absolute;
    left: 122px;
    top: 458px;
    margin: 0;
    padding: 0;
    list-style: none;
    font-size: 24px;
    line-height: 33px;
    letter-spacing: 0.4px;
  }
  .card__company {
    position: absolute;
    left: 116px;
    top: 656px;
    display: flex;
    align-items: center;
    gap: 16px;
  }
  .card__company-dot {
    width: 55px;
    height: 55px;
    border-radius: 50%;
    background: var(--navy);
  }
  .card__company-name {
    font-family: "Bodoni Moda", serif;
    font-weight: 500;
    font-size: 24px;
    color: var(--navy);
  }
</style>
</head>
<body>
  <div class="card">
    <svg class="card__shapes" width="1200" height="771" viewBox="0 0 1200 771" aria-hidden="true">
      <polygon fill="#1c6b2c" points="0,0 485,0 88,97 0,28"/>
      <polygon fill="#1c6b2c" points="1116,0 1200,0 1200,409 995,312"/>
      <polygon fill="#1c6b2c" points="0,706 247,771 0,771"/>
    </svg>

    <div class="card__portrait" role="img" aria-label="Portrait photo of Marisa Delgado, smiling, in a green dress with a gold necklace"></div>

    <h1 class="card__name">Marisa Delgado</h1>
    <p class="card__title">account executive | vice president</p>
    <div class="card__rule"></div>

    <p class="card__phone">909 555 0182</p>
    <ul class="card__links">
      <li>MDelgado@hdac.com</li>
      <li>Marisa.HarborlineIE.com</li>
    </ul>

    <div class="card__company">
      <span class="card__company-dot"></span>
      <span class="card__company-name">Harborline Deed Assurance Corp.</span>
    </div>
  </div>
</body>
</html>
```